Business Card Design for company

We want new business cards. We'd like something different-- yet still highly professional. Our tagline is Providing leadership, delivering success. Stock photos are ok, as long as they are relevant and look upscale.

Target Market(s)

Architecture/Business Management Consulting/Engineering Consulting

Contact Information for Business Card

dark gray background with pops of blue might be good, but you tell me. You're the designers. Rounded corners might be nice, but again, you tell me.

Font styles to use
Serif
Sans Serif

Colors
3276b5
5c5c5c
9d9d9d
fbfbfb

Requirements
Nice to have
• Something different, but still very professional.

```html
<!DOCTYPE html>
<html lang="en">
<head>
<meta charset="utf-8">
<title>Halden Partners – Business Cards</title>
<link rel="stylesheet" href="https://fonts.googleapis.com/css2?family=Roboto:wght@400;500;700&display=swap">
<style>
  :root {
    --blue: #3276b5;
    --blue-deep: #2a5f97;
    --slate: #474b52;
    --gray: #5c5c5c;
    --gray-light: #9d9d9d;
    --paper: #fbfbfb;
    --stage: #e4e5e7;
  }
  * { box-sizing: border-box; margin: 0; padding: 0; }
  html, body { width: 1200px; height: 768px; overflow: hidden; }
  body {
    background: var(--stage);
    font-family: "Roboto", Arial, sans-serif;
    position: relative;
  }
  .card {
    position: absolute;
    width: 525px;
    height: 300px;
    border-radius: 6px;
    overflow: hidden;
    box-shadow: 0 6px 18px rgba(0,0,0,0.18);
  }
  /* Back */
  .card-back {
    left: 45px; top: 234px;
    background: var(--slate);
    color: var(--paper);
  }
  .card-back .brand-name {
    position: absolute; left: 0; right: 0; top: 96px;
    text-align: center;
    font-weight: 500; font-size: 54px; letter-spacing: 6px;
  }
  .card-back .tagline {
    position: absolute; left: 0; right: 0; bottom: 52px;
    text-align: center;
    font-size: 14px; letter-spacing: 0.5px;
  }
  /* Front */
  .card-front {
    left: 630px; top: 234px;
    background: var(--paper);
    color: var(--gray);
  }
  .front-logo {
    position: absolute; right: 38px; top: 42px;
    font-weight: 500; font-size: 30px; letter-spacing: 2px;
    color: var(--blue);
    text-align: right;
    line-height: 1;
  }
  .person { position: absolute; left: 38px; top: 64px; }
  .person-name {
    color: var(--blue); font-weight: 700; font-size: 19px; letter-spacing: 0.5px;
  }
  .person-title { font-size: 12px; letter-spacing: 0.5px; margin-top: 2px; }
  .divider {
    position: absolute; left: 38px; right: 38px; top: 104px;
    height: 1px; background: var(--gray);
  }
  .contact-list { position: absolute; left: 38px; top: 118px; list-style: none; }
  .contact-list li {
    display: flex; align-items: center; gap: 8px;
    font-size: 12px; line-height: 19px;
  }
  .contact-list svg { width: 11px; height: 11px; fill: var(--blue); flex: none; }
  .address {
    position: absolute; right: 38px; top: 192px;
    text-align: right; font-size: 13px; line-height: 18px;
  }
  .footer-bands { position: absolute; left: 0; bottom: 0; width: 525px; height: 50px; }
  .website {
    position: absolute; right: 38px; bottom: 9px;
    color: var(--paper); font-size: 14px; letter-spacing: 0.3px;
  }
</style>
</head>
<body>

  <section class="card card-back" aria-label="Card back">
    <div class="brand-name">HALDEN</div>
    <p class="tagline">Providing leadership, delivering success</p>
  </section>

  <section class="card card-front" aria-label="Card front">
    <div class="front-logo">HALDEN PARTNERS</div>

    <div class="person">
      <div class="person-name">DANIEL REYES</div>
      <div class="person-title">CEO/FOUNDER</div>
    </div>

    <div class="divider"></div>

    <ul class="contact-list">
      <li><svg viewBox="0 0 24 24"><path d="M6.6 10.8a15 15 0 0 0 6.6 6.6l2.2-2.2a1 1 0 0 1 1-.25 11.4 11.4 0 0 0 3.6.57 1 1 0 0 1 1 1V20a1 1 0 0 1-1 1A17 17 0 0 1 3 4a1 1 0 0 1 1-1h3.5a1 1 0 0 1 1 1c0 1.25.2 2.45.57 3.57a1 1 0 0 1-.25 1z"/></svg>555 210 4417</li>
      <li><svg viewBox="0 0 24 24"><path d="M7 1h10a2 2 0 0 1 2 2v18a2 2 0 0 1-2 2H7a2 2 0 0 1-2-2V3a2 2 0 0 1 2-2zm0 3v14h10V4zm5 15.5a1 1 0 1 0 0 2 1 1 0 0 0 0-2z"/></svg>555 318 2096</li>
      <li><svg viewBox="0 0 24 24"><path d="M6 2h12v6H6zM4 9h16a2 2 0 0 1 2 2v7h-4v4H6v-4H2v-7a2 2 0 0 1 2-2zm4 7v4h8v-4z"/></svg>555 742 6083</li>
      <li><svg viewBox="0 0 24 24"><path d="M2 5h20v14H2zm2 2v.5l8 5 8-5V7zm0 3v7h16v-7l-8 5z"/></svg>daniel@haldenpartners.com</li>
    </ul>

    <div class="address">2140 Cedar Ridge Road<br>Portland, Oregon 97205</div>

    <svg class="footer-bands" viewBox="0 0 525 50" aria-hidden="true">
      <polygon points="0,20 250,20 262,34 0,34" fill="#5c5c5c"/>
      <polygon points="0,34 262,34 264,37 0,37" fill="#3276b5"/>
      <polygon points="262,37 275,14 525,14 525,50 0,50 0,37" fill="#3276b5"/>
    </svg>
    <div class="website">www.haldenpartners.com</div>
  </section>

</body>
</html>
```